Harbor Bloom Nutraceutical Website

Need a website for a vitamin gummy manufacturing and white-labeling company based in Charleston, SC. We service Zelvorn brands, Ecommerce brands, and any customer needing supplement gummies white labeled. I added out logos for color and style. We have always used navy blue, gold, and white in our color palet, we decided to add purple into the logo.

Our partner's website, that makes caples and powders, is https://www.brelmoxworks.com/

We are just now moving into our facility and don't have pictures or videos of the space, equipement, products, etc. I attached the flyer for the machine we have as reference.

The site just needs to be a simple landing page for now. 'Request Quote' for sales leads and 'enquire here' for job applications. I just need a simple site so we can have our state's dept of commerce announce us publicly.

There are 2 logos. We will be using 'Harbor Bloom Nutraceutical' for now. I cannot use "HB Nutra" until I have approval from our state, but "HB nutra" will be the end logo for use after a couple of months.

```html
<!DOCTYPE html>
<html lang="en">
<head>
<meta charset="utf-8">
<title>Harbor Bloom Nutraceutical</title>
<link rel="stylesheet" href="https://fonts.googleapis.com/css2?family=Montserrat:wght@500;600;700;800&family=Figtree:wght@400;500;600;700&display=swap">
<style>
:root{
  --purple:#6b11a9;
  --purple-deep:#5a0a96;
  --purple-soft:#efe3f4;
  --navy:#22306b;
  --ink:#111111;
  --text:#1d1d1d;
  --white:#ffffff;
  --footer:#1c1c1e;
  --footer-line:#8a8a8a;
}
*{margin:0;padding:0;box-sizing:border-box}
html,body{width:1200px;height:2880px;overflow:hidden}
body{font-family:"Figtree",sans-serif;color:var(--text);background:var(--white);position:relative}
.abs{position:absolute}
.display{font-family:"Montserrat",sans-serif;font-weight:800;letter-spacing:.5px}

/* top bar */
.topbar{left:0;top:0;width:1200px;height:43px;background:var(--purple);color:var(--white);font-size:12.5px;font-weight:700;letter-spacing:.3px}
.topbar .call{left:111px;top:14px}
.topbar .account{right:112px;top:13px;display:flex;align-items:center;gap:14px}
.topbar .sep{width:2px;height:18px;background:var(--white)}
.topbar .cart{display:flex;align-items:center;gap:8px}

/* header */
.header{left:0;top:43px;width:1200px;height:93px;background:var(--white)}
.nav-link{font-size:14px;color:var(--ink);top:39px}
.brand{left:390px;top:13px;width:420px;text-align:center;color:var(--purple);font-family:"Montserrat",sans-serif;font-weight:600;line-height:1}
.brand .l1{font-size:34px;letter-spacing:3px}
.brand .l2{font-size:25px;letter-spacing:4px;margin-top:6px}

/* hero */
.hero{left:0;top:136px;width:1200px;height:600px;background:
  radial-gradient(circle at 940px 270px,#e9a04a 0,#b5793f 110px,transparent 240px),
  radial-gradient(circle at 640px 420px,#9a6a52 0,transparent 200px),
  radial-gradient(circle at 1080px 120px,#f3b65c 0,transparent 120px),
  linear-gradient(100deg,#2f3a3f 0%,#4a4a3a 35%,#6b5136 60%,#2f4a4f 100%)}
.hero h1{left:111px;top:146px;color:var(--white);font-size:40px;line-height:53px;font-family:"Montserrat",sans-serif;font-weight:700;letter-spacing:1.5px}
.hero p{left:110px;top:312px;width:480px;color:var(--white);font-size:16px;line-height:24px;font-weight:500}
.btn{display:flex;align-items:center;justify-content:center;border-radius:22px;font-family:"Montserrat",sans-serif;font-weight:700;font-size:15.5px;letter-spacing:.3px}
.btn-light{background:var(--white);color:var(--ink)}
.btn-purple{background:var(--purple);color:var(--white)}
.btn-light-purple{background:var(--white);color:var(--purple)}

/* about */
.about-back{left:112px;top:826px;width:361px;height:290px;background:var(--purple-soft);border-radius:6px}
.about-photo{left:134px;top:849px;width:362px;height:291px;border-radius:6px;background:linear-gradient(135deg,#d9cbb8 0%,#b7a58f 40%,#2b3550 60%,#e7ddd0 100%)}
.about h2{left:600px;top:828px;font-size:40px;color:var(--ink)}
.about p{left:600px;top:892px;width:482px;font-size:16px;line-height:24px}

/* job band */
.jobs{left:0;top:1232px;width:1200px;height:300px;background:
  radial-gradient(circle at 80px 150px,#7c2cb4 0,transparent 160px),
  radial-gradient(circle at 1130px 180px,#7e2bb8 0,transparent 180px),
  linear-gradient(90deg,#6a14ab,#6d15ad 50%,#6a14ab);color:var(--white);text-align:center}
.jobs h2{left:0;top:42px;width:1200px;font-size:40px}
.jobs p{left:130px;top:106px;width:940px;font-size:16px;line-height:24px;font-weight:500}

/* products */
.products h2{left:0;top:1604px;width:1200px;text-align:center;font-size:40px;color:var(--ink)}
.products .lead{left:160px;top:1682px;width:880px;text-align:center;font-size:16px;line-height:24px}
.card{width:294px;height:470px;top:1770px;background:var(--white);border-radius:6px;box-shadow:0 3px 10px rgba(0,0,0,.12);overflow:hidden}
.card .photo{width:294px;height:290px}
.card h3{position:absolute;top:311px;width:100%;text-align:center;font-family:"Montserrat",sans-serif;font-weight:700;font-size:21px;color:var(--navy);letter-spacing:.3px}
.card .price{position:absolute;top:354px;width:100%;text-align:center;font-size:16px;font-weight:500}
.cart-btn{position:absolute;top:398px;left:76px;width:142px;height:41px;border:1px solid var(--navy);display:flex;font-size:12.5px;color:var(--ink);font-weight:500}
.cart-btn .ico{width:38px;border-right:1px solid var(--navy);display:flex;align-items:center;justify-content:center}
.cart-btn .lbl{flex:1;display:flex;align-items:center;justify-content:center}
.cart-btn.solid{background:var(--navy);color:var(--white);justify-content:center;align-items:center}

/* footer */
.footer{left:0;top:2408px;width:1200px;height:472px;background:radial-gradient(circle at 300px 200px,#2a2a2c 0,transparent 400px),var(--footer);color:var(--white)}
.footer .brand{top:50px;color:var(--white)}
.fcol h4{font-family:"Figtree",sans-serif;font-weight:700;font-size:16.5px;letter-spacing:.6px}
.fcol .item{font-size:16px;line-height:21px;letter-spacing:.3px}
.mail{left:109px;top:226px;width:175px;height:36px;background:var(--white);border-radius:2px;color:#222;font-size:10px;display:flex;align-items:center;padding-left:20px}
.socials{left:114px;top:365px;display:flex;gap:23px}
.socials span{width:20px;height:20px;border-radius:50%;background:var(--white);display:block}
.rule{left:111px;top:2805px;width:977px;height:1px;background:var(--footer-line)}
.copyright{left:0;top:2826px;width:1200px;text-align:center;color:var(--white);font-size:16.5px;letter-spacing:.6px}
</style>
</head>
<body>

<div class="abs topbar">
  <div class="abs call">QUESTIONS? CALL US: +1(555) 010 0199</div>
  <div class="abs account">
    <span>LOGIN</span><span class="sep"></span>
    <span class="cart">
      <svg width="22" height="18" viewBox="0 0 22 18" fill="none" stroke="#fff" stroke-width="1.5"><path d="M1 2h3l3 10h11l2-7H5.5"/><path d="M8 6h11M8.5 9h9.5M10 5v7M13 5v7M16 5v7"/><circle cx="9" cy="15.5" r="1.3"/><circle cx="16.5" cy="15.5" r="1.3"/></svg>
      CART:0
    </span>
  </div>
</div>

<header class="abs header">
  <span class="abs nav-link" style="left:111px">Home</span>
  <span class="abs nav-link" style="left:190px">About Us</span>
  <div class="abs brand"><div class="l1">HARBOR BLOOM</div><div class="l2">NUTRACEUTICAL</div></div>
  <span class="abs nav-link" style="left:903px">Our Products</span>
  <span class="abs nav-link" style="left:1031px">Contacts</span>
</header>

<section class="abs hero" role="img" aria-label="Smiling girl holding a bowl of berries beside a glass jar of colourful gummies, warm bokeh lights behind">
  <h1 class="abs">WELCOME TO<br>HARBOR BLOOM<br>NUTRACEUTICAL</h1>
  <p class="abs">Lorem ipsum dolor sit amet, consectetur adipiscing elit, sed do eiusmod tempor incididunt ut labore et dolore magna aliqua. Ut enim ad minim veniam</p>
  <a class="abs btn btn-light" style="left:111px;top:407px;width:199px;height:39px">REQUEST A QUOTE</a>
</section>

<section class="about">
  <div class="abs about-back"></div>
  <div class="abs about-photo" role="img" aria-label="Young girl in a kitchen holding green gummies, pastries and milk on the table"></div>
  <h2 class="abs display">ABOUT US</h2>
  <p class="abs">Lorem ipsum dolor sit amet, consectetur adipiscing elit, sed do eiusmod tempor incididunt ut labore et dolore magna aliqua. Ut enim ad minim veniam, quis nostrud exercitation ullamco laboris nisi ut aliquip ex ea commodo consequat. Duis aute irure dolor in reprehenderit in voluptate velit esse cillum dolore eu fugiat nulla pariatur. Excepteur sint occaecat cupidatat non proident, sunt in culpa qui officia deserunt mollit anim id est laborum</p>
  <a class="abs btn btn-purple" style="left:600px;top:1092px;width:156px;height:39px">ORDER NOW</a>
</section>

<section class="abs jobs">
  <h2 class="abs display">JOB APPLICATION</h2>
  <p class="abs">Lorem ipsum dolor sit amet, consectetur adipiscing elit, sed do eiusmod tempor incididunt ut labore et dolore magna aliqua. Ut enim ad minim veniam, quis nostrud exercitation ullamco laboris nisi ut aliquip ex ea commodo consequat. Duis aute irure dolor sunt in culpa qui officia deserunt mollit anim id est laborum</p>
  <a class="abs btn btn-light-purple" style="left:496px;top:210px;width:207px;height:38px">ENQUIRY NOW</a>
</section>

<section class="products">
  <h2 class="abs display">OUR PRODUCTS</h2>
  <p class="abs lead">Lorem ipsum dolor sit amet, consectetur adipiscing elit, sed do eiusmod tempor incididunt ut labore et dolore magna aliqua. Ut enim ad minim veniam</p>

  <article class="abs card" style="left:112px">
    <div class="photo" role="img" aria-label="Hand holding two sugar-coated fruit gummies in front of green leaves" style="background:linear-gradient(180deg,#3e5a34 0%,#6f7f52 40%,#e8b59a 65%,#f0d2c0 100%)"></div>
    <h3>GUMMY BEARS</h3>
    <div class="price">$7.99 – $9.99</div>
    <div class="cart-btn"><span class="ico"><svg width="22" height="18" viewBox="0 0 22 18" fill="none" stroke="#22306b" stroke-width="1.5"><path d="M1 2h3l3 10h11l2-7H5.5"/><path d="M8 6h11M8.5 9h9.5M10 5v7M13 5v7M16 5v7"/><circle cx="9" cy="15.5" r="1.3"/><circle cx="16.5" cy="15.5" r="1.3"/></svg></span><span class="lbl">ADD TO CART</span></div>
  </article>

  <article class="abs card" style="left:453px">
    <div class="photo" role="img" aria-label="Pile of assorted sour gummy candies in bright colours" style="background:linear-gradient(135deg,#e8434f 0%,#f2a53a 30%,#5fb7e0 55%,#e3e04a 75%,#e6477a 100%)"></div>
    <h3>TANGLE SOUR</h3>
    <div class="price">$7.99 – $9.99</div>
    <div class="cart-btn solid">ADD TO CART</div>
  </article>

  <article class="abs card" style="left:794px">
    <div class="photo" role="img" aria-label="Close-up of red, orange and dark berry gummies" style="background:linear-gradient(135deg,#4a1a2a 0%,#b4162a 35%,#e84a2a 60%,#f08a2a 80%,#d8202a 100%)"></div>
    <h3>SUN BEAR</h3>
    <div class="price">$7.99 – $9.99</div>
    <div class="cart-btn"><span class="ico"><svg width="22" height="18" viewBox="0 0 22 18" fill="none" stroke="#22306b" stroke-width="1.5"><path d="M1 2h3l3 10h11l2-7H5.5"/><path d="M8 6h11M8.5 9h9.5M10 5v7M13 5v7M16 5v7"/><circle cx="9" cy="15.5" r="1.3"/><circle cx="16.5" cy="15.5" r="1.3"/></svg></span><span class="lbl">ADD TO CART</span></div>
  </article>

  <a class="abs btn btn-purple" style="left:522px;top:2284px;width:156px;height:38px">VIEW MORE</a>
</section>

<footer class="abs footer">
  <div class="abs brand"><div class="l1">HARBOR BLOOM</div><div class="l2">NUTRACEUTICAL</div></div>

  <div class="abs fcol" style="left:109px;top:182px">
    <h4>NEWSLETTER SIGNUP</h4>
  </div>
  <div class="abs mail">Enter Mail Address
    <svg style="position:absolute;right:20px;top:8px" width="22" height="20" viewBox="0 0 22 20"><path d="M1 9 21 1 15 19 11 11Z" fill="#111"/><path d="M11 11 21 1" stroke="#fff" stroke-width="1.2"/></svg>
  </div>
  <div class="abs fcol" style="left:111px;top:284px;width:190px"><div class="item">Lorem ipsum dolor sit amet, consectetur adipiscing elit, magna</div></div>
  <div class="abs socials"><span></span><span></span><span></span><span></span><span></span></div>

  <div class="abs fcol" style="left:383px;top:182px">
    <h4>BUSINESS HOURS</h4>
  </div>
  <svg class="abs" style="left:383px;top:240px" width="22" height="22" viewBox="0 0 22 22" fill="none" stroke="#fff" stroke-width="1.4"><circle cx="11" cy="11" r="9.5"/><path d="M11 5v6l-4 3"/></svg>
  <div class="abs fcol" style="left:415px;top:225px"><div class="item">Monday to Friday,<br>8 AM to 5 PM</div></div>
  <div class="abs fcol" style="left:382px;top:286px"><h4>VISIT US ONLINE</h4></div>
  <svg class="abs" style="left:383px;top:318px" width="22" height="22" viewBox="0 0 22 22" fill="none" stroke="#fff" stroke-width="1.3"><circle cx="11" cy="11" r="9.5"/><ellipse cx="11" cy="11" rx="4" ry="9.5"/><path d="M1.5 11h19M3 6h16M3 16h16"/></svg>
  <div class="abs fcol" style="left:417px;top:318px"><div class="item" style="text-decoration:underline">shop.harborbloom.com</div></div>

  <div class="abs fcol" style="left:659px;top:182px"><h4>CONTACTS</h4></div>
  <svg class="abs" style="left:662px;top:227px" width="18" height="26" viewBox="0 0 18 26" fill="none" stroke="#fff" stroke-width="1.4"><path d="M9 25S1 14 1 9a8 8 0 0 1 16 0c0 5-8 16-8 16Z"/><circle cx="9" cy="9" r="3"/></svg>
  <div class="abs fcol" style="left:698px;top:225px"><div class="item">United States,<br>New York</div></div>
  <svg class="abs" style="left:662px;top:284px" width="22" height="16" viewBox="0 0 22 16" fill="none" stroke="#fff" stroke-width="1.4"><rect x="1" y="1" width="20" height="14" rx="2"/><path d="M1 2l10 7 10-7"/></svg>
  <div class="abs fcol" style="left:698px;top:281px"><div class="item">info@harborbloom.com</div></div>
  <svg class="abs" style="left:661px;top:322px" width="24" height="24" viewBox="0 0 24 24" fill="none" stroke="#fff" stroke-width="1.4"><path d="M5 2l4 5-2 3c1 3 4 6 7 7l3-2 5 4-2 3C12 22 2 12 2 4Z"/><path d="M14 2a8 8 0 0 1 8 8M14 6a4 4 0 0 1 4 4"/></svg>
  <div class="abs fcol" style="left:698px;top:325px"><div class="item" style="font-size:15px">+1(555) 010 0199</div></div>

  <div class="abs fcol" style="left:939px;top:182px">
    <h4>ABOUT COMPANY</h4>
    <div class="item" style="margin-top:14px;line-height:26px">Home<br>About us<br>Services<br>Our Products<br>Contacts</div>
  </div>
</footer>
<div class="abs rule"></div>
<div class="abs copyright">Copyrights © 2024 Harbor Bloom Nutraceutical -Privacy Policy - All Rights Reserved</div>

</body>
</html>
```